Corvane Holdings needs a business card

I would like the card to be simple but modern and elegant.
I like black and white.
or black and gold.
we are a private finance lender and also are involved in property and property developments.

please look at the business card photos i provided i would like C.H only one one side and all the other details on the other side use fonts that tie in with my theme.

Industry/Entity Type

Finance

Contact Information for Business Card

Corvane Holdings (C.H) Elliot Marbury M: 0413586102 E: elliotmar@examplemail.net

Font styles to use
Other font styles liked:
• Use fonts that would reflect our business

Colors
000000
ffffff

Requirements
Must have
• one side of details
• other side has either C.H or Corvane Holdings like in the photos provided

```html
<!DOCTYPE html>
<html lang="en">
<head>
<meta charset="utf-8">
<title>Corvane Holdings – Business Card</title>
<link rel="stylesheet" href="https://fonts.googleapis.com/css2?family=Sorts+Mill+Goudy&display=swap">
<style>
  :root {
    --ink: #000000;
    --paper: #ffffff;
    --gold: #857449;
  }
  * { box-sizing: border-box; margin: 0; padding: 0; }
  html, body {
    width: 960px;
    height: 1200px;
    overflow: hidden;
    background: var(--paper);
  }
  body {
    position: relative;
    font-family: "Sorts Mill Goudy", Georgia, serif;
    color: var(--gold);
  }
  .card {
    position: absolute;
    left: 60px;
    width: 840px;
    height: 480px;
    background: var(--ink);
  }
  .card--front { top: 94px; }
  .card--back  { top: 642px; }

  .card__frame {
    position: absolute;
    inset: 16px 14px 14px 15px;
    border: 6px double var(--gold);
  }

  /* Front */
  .front__panel {
    position: absolute;
    left: 100px;
    top: 72px;
    width: 640px;
    height: 336px;
    border: 1.5px solid var(--gold);
  }
  .front__rule {
    position: absolute;
    top: 236px;
    height: 8.5px;
    border-top: 1.5px solid var(--gold);
    border-bottom: 1.5px solid var(--gold);
  }
  .front__rule--left  { left: 101px; width: 180px; }
  .front__rule--right { left: 558px; width: 181px; }
  .front__name {
    position: absolute;
    left: 281px;
    width: 277px;
    top: 240px;
    transform: translateY(-50%);
    text-align: center;
    font-size: 54px;
    line-height: 1.08;
    color: var(--gold);
  }

  /* Back */
  .back__details {
    position: absolute;
    inset: 0;
    text-align: center;
  }
  .back__name {
    position: absolute;
    left: 0;
    right: 0;
    top: 194px;
    font-size: 40px;
    line-height: 40px;
  }
  .back__name span {
    display: inline-block;
    padding: 0 6px 12px;
    border-bottom: 2.5px solid var(--gold);
  }
  .back__line {
    position: absolute;
    left: 0;
    right: 0;
    font-size: 37px;
    line-height: 37px;
  }
  .back__line--phone { top: 282px; }
  .back__line--email { top: 354px; }
</style>
</head>
<body>
  <section class="card card--front" aria-label="Card front">
    <div class="card__frame"></div>
    <div class="front__panel"></div>
    <div class="front__rule front__rule--left"></div>
    <div class="front__rule front__rule--right"></div>
    <p class="front__name">Corvane<br>Holdings</p>
  </section>

  <section class="card card--back" aria-label="Card back">
    <div class="card__frame"></div>
    <div class="back__details">
      <p class="back__name"><span>Elliot Marbury</span></p>
      <p class="back__line back__line--phone">M: 0413586102</p>
      <p class="back__line back__line--email">E: elliotmar@examplemail.net</p>
    </div>
  </section>
</body>
</html>
```